Business Card Design Project

Hello
I want a Simple Business card that uses the company logo that is easily reasonable but looks professional as I am an IT Services company and would look to share these cards with prospective clients.
The details are:
Kestrel Arc Solutions
14 Morrow Lane
Birmingham
B7 4QX
Telephone 0845 217 6640
I would like my name Oliver Hastings and my title Director on the card.
Target Market(s)
IT Professionals
Industry/Entity Type
Business

```html
<!DOCTYPE html>
<html lang="en">
<head>
<meta charset="utf-8">
<title>Kestrel Arc Solutions – Business Card</title>
<link href="https://fonts.googleapis.com/css2?family=Open+Sans:wght@400;600&display=swap" rel="stylesheet">
<style>
  :root {
    --backdrop: #e6e6e6;
    --card-green: #66962f;
    --band-black: #1d1d1b;
    --ink-dark: #262626;
    --ink-light: #ffffff;
    --accent-lime: #c8d84a;
  }
  * { box-sizing: border-box; margin: 0; padding: 0; }
  html, body {
    width: 1200px; height: 1200px; overflow: hidden;
    background: var(--backdrop);
    font-family: "Open Sans", Arial, sans-serif;
  }
  .canvas {
    width: 1200px; height: 1200px;
    display: flex; align-items: center; justify-content: center;
  }
  .business-card {
    position: relative;
    width: 1000px; height: 571px;
    background: var(--card-green);
    overflow: hidden;
    box-shadow: 0 10px 30px rgba(0,0,0,0.15);
  }
  .brand-band {
    position: absolute; left: 0; top: 132px;
    width: 80px; height: 46px;
    background: var(--band-black);
  }
  .brand-name {
    position: absolute; left: 96px; top: 120px;
    display: flex; align-items: center; gap: 16px;
    font-size: 46px; font-weight: 600;
    color: var(--ink-dark); letter-spacing: -0.5px;
    white-space: nowrap;
  }
  .brand-dot {
    width: 38px; height: 38px; border-radius: 50%;
    background: var(--accent-lime);
  }
  .name-band {
    position: absolute; left: 520px; right: 0; top: 290px;
    height: 74px;
    background: var(--band-black);
    padding: 10px 0 0 20px;
    color: var(--ink-light);
  }
  .person-name { font-size: 30px; font-weight: 600; line-height: 1.1; }
  .person-title { font-size: 16px; font-weight: 400; line-height: 1.3; }
  .contact-list {
    position: absolute; left: 532px; top: 386px;
    list-style: none;
    font-size: 22px; line-height: 30px;
    color: var(--ink-dark);
  }
  .contact-item { display: flex; gap: 10px; align-items: flex-start; }
  .contact-icon { flex: none; margin-top: 5px; }
</style>
</head>
<body>
<main class="canvas">
  <article class="business-card">
    <div class="brand-band"></div>
    <div class="brand-name">Kestrel Arc Solutions<span class="brand-dot"></span></div>

    <div class="name-band">
      <p class="person-name">Oliver Hastings</p>
      <p class="person-title">Director</p>
    </div>

    <ul class="contact-list">
      <li class="contact-item">
        <svg class="contact-icon" width="20" height="20" viewBox="0 0 20 20" aria-hidden="true">
          <circle cx="10" cy="10" r="10" fill="#262626"/>
          <path d="M5 10.5 L10 6 L15 10.5 H13.5 V14.5 H6.5 V10.5 Z" fill="#66962f"/>
        </svg>
        <span>14 Morrow Lane,<br>Birmingham, B7 4QX</span>
      </li>
      <li class="contact-item">
        <svg class="contact-icon" width="20" height="20" viewBox="0 0 20 20" aria-hidden="true">
          <circle cx="10" cy="10" r="10" fill="#262626"/>
          <rect x="7" y="4.5" width="6" height="11" rx="1" fill="#66962f"/>
          <rect x="8" y="6" width="4" height="6" fill="#262626"/>
        </svg>
        <span>0845 217 6640</span>
      </li>
    </ul>
  </article>
</main>
</body>
</html>
```